Premium Audio and HD Video with AFS!

AFS is a mobile studio that provides premium audio and HD video recording for the classical and jazz community in the Boston area. Specializing in concerts, recitals, auditions, studio releases, lectures, podcasts and more.
My website:
http://amberfieldsoundworks.example
https://www.facebook.com/AFSoundworks/
Target Market(s)
classical and jazz instrumentalists, vocalists, ensembles, choruses, a cappella groups, podcasters
Industry/Entity Type
Audio
Font styles to use
Serif
Colors
Designer to choose colors to be used in the design.
Requirements
Must have
- My logo!
- Must convey that this mobile recording studio is for classical and jazz musicians... not rock bands etc.
- I provide event recording as well as "studio recording" (for CDs etc)
- Eye catching
- Must be scalable for different size flyers... full page, half page etc
- I will use it for bulletin boards.. so the front side is most important... if the design is two sided, the lesser important info should be on the back side.
Nice to have
- Use some of the photos on my facebook page? Not sure they are high res or decent photos..
- https://www.facebook.com/AFSoundworks/
Should not have
- Anything depicting a rock band or similar

```html
<!DOCTYPE html>
<html lang="en">
<head>
<meta charset="utf-8">
<title>Amberfield Soundworks – Flyer</title>
<link href="https://fonts.googleapis.com/css2?family=Montserrat:wght@400;500;600;700&family=Righteous&display=swap" rel="stylesheet">
<style>
:root{
  --green:#4a8c66;
  --green-text:#2f7a4c;
  --black:#151614;
  --grey-dark:#6e6f71;
  --grey-light:#a3a4a6;
  --paper:#ffffff;
  --panel:#f1f1f1;
  --ink:#1d1d1d;
  --stage:#e8e5e0;
  --social:#2b6fb0;
}
*{margin:0;padding:0;box-sizing:border-box}
html,body{width:1200px;height:903px;overflow:hidden}
body{background:var(--stage);font-family:"Montserrat",Arial,sans-serif;color:var(--ink);position:relative}
.flyer{position:absolute;top:80px;width:526px;height:744px;background:var(--paper);overflow:hidden;box-shadow:0 4px 14px rgba(0,0,0,.25)}
.flyer--front{left:53px}
.flyer--back{left:622px}
.abs{position:absolute}

/* front */
.masthead{left:0;top:0;width:526px;height:150px;background:var(--black)}
.brand{left:0;top:52px;width:526px;text-align:center;color:#e8ece9;font-family:"Montserrat",sans-serif;font-weight:500;font-size:24px;letter-spacing:3px}
.frame{left:0;top:120px}
.hero-photo{left:27px;top:150px;width:472px;height:304px;background:radial-gradient(ellipse at 60% 45%,#8d8b89 0%,#6d6b69 55%,#5a5856 100%);border:2px solid #fff}
.headline-band{left:0;top:488px;width:526px;height:92px;background:var(--green);text-align:center;font-family:"Righteous",sans-serif;text-transform:uppercase}
.headline-band .line1{color:#fff;font-size:37px;line-height:40px;padding-top:8px}
.headline-band .line2{color:var(--black);font-size:37px;line-height:40px}
.intro{left:0;top:580px;width:526px;height:120px;background:var(--panel)}
.intro p{position:absolute;left:60px;width:406px;top:16px;text-align:center;font-size:11.4px;line-height:13px;font-weight:500}
.intro .occasions{top:82px;left:100px;width:326px;color:var(--green-text);font-weight:600;font-size:12.4px;line-height:15px}
.follow{font-size:7.4px;font-weight:600;text-transform:uppercase;letter-spacing:.2px}
.follow .icons{display:flex;gap:3px;margin-top:3px}
.follow .icons span{width:13px;height:13px;background:var(--social);border-radius:2px;display:block}
.footer{left:0;top:700px;width:526px;height:44px;background:var(--black);color:#f2f2f2;display:flex;align-items:center;justify-content:center;gap:14px;font-size:8.2px;white-space:nowrap}
.footer .item{display:flex;align-items:center;gap:5px}
.footer .phone{font-size:11px}
.footer svg{width:12px;height:12px;stroke:var(--green);fill:none;stroke-width:1.6;flex:none}

/* back */
.services-head{left:0;top:0;width:526px;height:158px;background:var(--green);color:#fff;text-align:center}
.services-head h2{font-size:14px;font-weight:700;margin-top:26px;letter-spacing:.2px}
.services-head h3{font-size:13.6px;font-weight:500;margin-top:6px;letter-spacing:.4px}
.services-head p{position:absolute;left:24px;top:70px;width:478px;font-size:7.3px;line-height:9.4px;text-align:justify}
.service h4{position:absolute;font-size:12.4px;font-weight:500;letter-spacing:.6px}
.service p{position:absolute;font-size:7.6px;line-height:9.6px;text-align:justify}
.thumb{position:absolute}
.back-follow{left:352px;top:686px;display:flex;align-items:center;gap:10px}
.back-follow .icons{margin-top:0}
</style>
</head>
<body>

<section class="flyer flyer--front">
  <div class="abs masthead"></div>
  <div class="abs brand">Amberfield Soundworks</div>

  <svg class="abs frame" width="526" height="368" viewBox="0 0 526 368" aria-hidden="true">
    <polygon points="0,0 27,30 27,334 0,368" fill="var(--grey-dark)"/>
    <polygon points="526,0 499,30 499,334 526,368" fill="var(--grey-dark)"/>
    <polygon points="0,368 27,334 499,334 526,368" fill="var(--grey-light)"/>
    <polyline points="0,0 27,30" stroke="#fff" stroke-width="1.5" fill="none"/>
    <polyline points="526,0 499,30" stroke="#fff" stroke-width="1.5" fill="none"/>
    <polyline points="0,368 27,334" stroke="#fff" stroke-width="1.5" fill="none"/>
    <polyline points="526,368 499,334" stroke="#fff" stroke-width="1.5" fill="none"/>
  </svg>
  <div class="abs hero-photo" role="img" aria-label="Singer wearing headphones performing into a studio condenser microphone against a grey backdrop"></div>

  <div class="abs headline-band">
    <div class="line1">Premium Audio &amp;</div>
    <div class="line2">HD Video with AFS!</div>
  </div>

  <div class="abs intro">
    <p>Serving the solo vocal/instrumental, chamber music, choral, orchestral, and contemporary acappella community in the Greater Boston area, Amberfield provides premium audio and 4K/HD video production services for...</p>
    <p class="occasions">Concerts, Recitals, Studio Releases, Auditions, Lectures, Podcasts &amp; More!</p>
    <div class="abs follow" style="left:439px;top:78px">Follow us on
      <div class="icons"><span></span><span></span><span></span><span></span></div>
    </div>
  </div>

  <div class="abs footer">
    <div class="item phone"><svg viewBox="0 0 16 16"><path d="M4 1.5l2.5 3-1.5 2a8 8 0 0 0 4.5 4.5l2-1.5 3 2.5-1.5 2.5C7 14.5 1.5 9 1.5 3z"/></svg>555.014.2290</div>
    <div class="item"><svg viewBox="0 0 16 16"><rect x="1.5" y="3.5" width="13" height="9"/><path d="M1.5 3.5l6.5 5 6.5-5"/></svg>hello@amberfieldsoundworks.example</div>
    <div class="item"><svg viewBox="0 0 16 16"><circle cx="8" cy="8" r="6.5"/><ellipse cx="8" cy="8" rx="3" ry="6.5"/><path d="M1.5 8h13"/></svg>www.amberfieldsoundworks.example</div>
  </div>
</section>

<section class="flyer flyer--back">
  <div class="abs services-head">
    <h2>OUR SERVICES</h2>
    <h3>COMPREHENSIVE APPROACH</h3>
    <p>Whether you wish to release a single audio demo track, produce an EP, turn out a full length CD, capture audio and video of a live event, or launch a podcast, AFS will be a partner to make your next project come to fruition. We start with a project discovery meeting/conference call where we have a guided discussion about the requirements and goals for your project including type, size, and timeline. AFS then takes this information and produces a detailed project proposal complete with project milestones, scheduling, pricing and any necessary materials... no hidden costs, no gotchas, no surprises, no fine print. We provide regular status updates to you as the project progresses. We are always available for feedback. Since we've been 'on the other side of the microphone', we understand this can be a daunting and often stressful process. Let our 20+ years in the field work for you!</p>
  </div>

  <article class="service">
    <h4 style="left:24px;top:176px">MOBILE STUDIO RECORDING</h4>
    <p style="left:24px;top:197px;width:326px">With a boatload of gear and the expertise to back it up, we bring the recording studio experience to you, in your own space, where you're most comfortable, at a fraction of the cost of renting out a traditional recording studio. With advances in physical and software tools, just about any relatively quiet space can be used as a recording studio. AFS will analyze your arrangement(s) and your environment to propose various tracking alternatives to use your recording session time in the most effective manner possible.</p>
    <div class="thumb" style="left:366px;top:178px;width:136px;height:116px;background:linear-gradient(135deg,#f4f4f4,#dcdcdc)" role="img" aria-label="Silver studio condenser microphone in a shock mount"></div>
  </article>

  <article class="service">
    <div class="thumb" style="left:24px;top:302px;width:136px;height:115px;background:linear-gradient(180deg,#b9b2a6 0%,#7c6f62 50%,#2e2824 100%)" role="img" aria-label="Choir performing to an audience in a bright concert hall"></div>
    <h4 style="left:176px;top:309px">EVENT RECORDING</h4>
    <p style="left:176px;top:330px;width:326px">Amberfield specializes in premium audio and 4K/FHD video recording for concerts, recitals, and mixed lecture/performance events. We offer multiple HD cameras and many configurations of stereo sound, as well as full 5.1 and 7.1 surround sound to perfectly capture your next musical event! Audio and video clips on popular social media and music streaming sites alike, can bring in bigger audiences as well as help recruit new members for your group!</p>
  </article>

  <article class="service">
    <h4 style="left:24px;top:454px">MIXING AND EDITING</h4>
    <p style="left:24px;top:476px;width:326px">Whether or not you have recorded the raw tracks with us, AFS provides extensive editing and mixing services using state of the art software tools for video editing, motion effects, audio restoration, mixing, mastering and pitch correction, plus a professional multitrack production suite. Our project based pricing guarantees top notch results without blowing out your budget.</p>
    <div class="thumb" style="left:366px;top:442px;width:136px;height:116px;background:linear-gradient(180deg,#2a3340 0%,#5d7f9c 45%,#dfe6ec 70%,#f4f4f4 100%)" role="img" aria-label="Screenshot of audio mixing and pitch editing software"></div>
  </article>

  <article class="service">
    <div class="thumb" style="left:24px;top:562px;width:136px;height:116px;background:linear-gradient(160deg,#3d4a52 0%,#27323a 55%,#161c21 100%)" role="img" aria-label="Close-up of a mastering plugin interface on a dark screen"></div>
    <h4 style="left:176px;top:569px">MASTERING</h4>
    <p style="left:176px;top:590px;width:326px">Know thy media! Back in the day, mastering was the process of taking final mixes and creating wax disc masters which were then used to make stampers to press shellac-composite 78 rpm records. Today, mastering refers to preparing your polished recordings for the final destination media. CDs, download stores, streaming services and video platforms all have their own little quirks and features. Amberfield is fluent in all forms of media... You've worked hard to make your recordings. We'll make sure they sound great wherever you plan to market/sell them.</p>
  </article>

  <div class="abs follow back-follow">Follow us on
    <div class="icons"><span></span><span></span><span></span><span></span></div>
  </div>

  <div class="abs footer">
    <div class="item phone"><svg viewBox="0 0 16 16"><path d="M4 1.5l2.5 3-1.5 2a8 8 0 0 0 4.5 4.5l2-1.5 3 2.5-1.5 2.5C7 14.5 1.5 9 1.5 3z"/></svg>555.014.2290</div>
    <div class="item"><svg viewBox="0 0 16 16"><rect x="1.5" y="3.5" width="13" height="9"/><path d="M1.5 3.5l6.5 5 6.5-5"/></svg>hello@amberfieldsoundworks.example</div>
    <div class="item"><svg viewBox="0 0 16 16"><circle cx="8" cy="8" r="6.5"/><ellipse cx="8" cy="8" rx="3" ry="6.5"/><path d="M1.5 8h13"/></svg>www.amberfieldsoundworks.example</div>
  </div>
</section>

</body>
</html>
```